Plakat-Design für Veltrana
Zielgruppe
Wir sind eine 'kreative' kleine Truppe, die mit neuen Ideen versuchen wollen, auch mal andere Wege in den Projekten zu gehen.
Aufgabenstellung
Für die Motivation meiner Mitarbeiter und für meinen Empfang suche ich Plakate in der Höhe von ca. 150 cm und Breite von etwa 50 cm.
Sie sollen die weißen Wände etwas auflockern, von daher hätte ich gern die Hauptfarbe im Hintergrund. Ansonsten bitte für die Farbakzente die CD-Farben nutzen.
Grundsätzlich soll das Thema "Einfach Machen" sein. Ich möchte damit animieren Dinge und Wege auszuprobieren, ohne vorab immer scheu davor zu haben.
Gerne auch mit weiteren Textvorschlägen. Pro neuen Text, der dann auf ein Poster kommt, zahle ich einen Bonus von 40€.

```html
<!DOCTYPE html>
<html lang="de">
<head>
<meta charset="utf-8">
<title>Einfach Machen – Veltrana</title>
<link rel="stylesheet" href="https://fonts.googleapis.com/css2?family=Barlow:wght@400;500;600&display=swap">
<style>
  :root {
    --bg: #434b4e;
    --accent: #ede87c;
    --copy: #b9b9be;
    --claim: #c9c9ce;
    --brand: #d9dee1;
  }
  html, body {
    margin: 0;
    padding: 0;
    width: 1200px;
    height: 3598px;
    overflow: hidden;
    background: var(--bg);
  }
  .poster {
    position: relative;
    width: 1200px;
    height: 3598px;
    background: var(--bg);
    font-family: "Barlow", sans-serif;
  }
  .headline {
    position: absolute;
    left: 0;
    top: 0;
    width: 1200px;
    height: 1400px;
  }
  .headline text {
    font-family: "Barlow", sans-serif;
    font-weight: 600;
    font-size: 233px;
    fill: var(--accent);
  }
  .quote {
    position: absolute;
    left: 0;
    top: 1371px;
    width: 1200px;
    margin: 0;
    text-align: center;
    font-size: 74px;
    line-height: 101px;
    font-weight: 600;
    letter-spacing: 1px;
    color: var(--copy);
    text-transform: uppercase;
  }
  .claim {
    position: absolute;
    left: 0;
    top: 3140px;
    width: 1200px;
    margin: 0;
    text-align: center;
    font-size: 62px;
    font-weight: 400;
    letter-spacing: 1px;
    color: var(--claim);
  }
  .brand {
    position: absolute;
    left: 0;
    top: 3260px;
    width: 1200px;
    margin: 0;
    text-align: center;
    font-size: 200px;
    line-height: 240px;
    font-weight: 500;
    color: var(--brand);
  }
</style>
</head>
<body>
<main class="poster">
  <svg class="headline" width="1200" height="1400" viewBox="0 0 1200 1400" aria-label="Einfach machen">
    <text class="headline-word" x="600" y="1036" text-anchor="middle" textLength="950" lengthAdjust="spacing" transform="rotate(180 600 954)">EINFACH</text>
    <text class="headline-word" x="600" y="1283" text-anchor="middle" textLength="940" lengthAdjust="spacing" transform="rotate(180 600 1200)">MACHEN</text>
  </svg>

  <p class="quote">Du bist ein Genie, wenn<br>du jedes Problem aus<br>unterschiedlichen<br>Perspektiven betrachtest.</p>

  <p class="claim">EINFACH MACHEN!</p>
  <p class="brand">Veltrana</p>
</main>
</body>
</html>
```